QuoteMarlin.com Homepage Redesign

Create a new homepage design for our website QuoteMarlin.com. Our current experience is focused on auto insurance only. We would like to incorporate the ability to receive rate estimates for home insurance and bundled (home + auto) insurance in addition to auto. Home insurance will include home, renters and condo. The final design should inspire users to utilize our comparison tool.

Industry/Entity Type

Insurance (Auto & Home)

Number of Pages Required

1 page

Font styles to use
Other font styles liked:
• See Assets - Sans Serif & Roboto

Colors
0054AA
0677BA
7BADD7
CADEEF
E8F1F8
59FF00
82FF00
B8FF75
E3FFCB
F4FFEA

Requirements
Must have
• Must include the ability to launch our rate comparison tool within the main hero image for Auto, Home, Bundled.
Nice to have
• The design should be bold and eye catching. It should be differentiated from the typical landing page experience. (Some of our favorite sites from a UX perspective include: Vaultline.org, ThePelican.com, Ferrow.com and Corvane Airways - They are busy but we like the app like approach on the homepage)
Should not have
• We are not looking for a design that is heavy on generic images.

```html
<!DOCTYPE html>
<html lang="en">
<head>
<meta charset="utf-8">
<title>Quote Marlin – Compare Insurance Rates</title>
<link href="https://fonts.googleapis.com/css2?family=Poppins:wght@300;400;500;600;700&display=swap" rel="stylesheet">
<style>
:root{
  --blue:#1463F3;
  --blue-dark:#0B4FD0;
  --orange:#FFB54D;
  --ink:#111111;
  --muted:#6B7280;
  --tint:#EEF4FD;
  --line:#CFDDF3;
  --white:#FFFFFF;
  --green:#3FBF6A;
  --red:#E66565;
}
*{box-sizing:border-box;margin:0;padding:0}
html,body{width:1200px;height:1200px;overflow:hidden}
body{font-family:'Poppins',sans-serif;color:var(--ink);background:var(--orange)}
.canvas{position:relative;width:1200px;height:1200px;overflow:hidden}
.backdrop{position:absolute;inset:0}
.abs{position:absolute}
.page{position:absolute;top:32px;height:1136px;background:var(--white);overflow:hidden}
.page-left{left:35px;width:634px}
.page-right{left:689px;width:476px}
.c{text-align:center}
.nav{position:absolute;left:0;top:0;width:634px;height:41px;border-bottom:2px solid #E3ECFA}
.brand{position:absolute;left:60px;top:11px;display:flex;align-items:center;gap:5px;font-weight:600;font-size:12.5px;color:var(--blue-dark)}
.brand-dot{width:9px;height:9px;background:var(--blue);border-radius:50%}
.nav-link{position:absolute;top:13px;font-size:9.5px;font-weight:500}
.btn{background:var(--blue);color:var(--white);font-weight:500;display:flex;align-items:center;justify-content:center}
.nav-btn{position:absolute;left:505px;top:10px;width:77px;height:20px;font-size:9px}
.badge{position:absolute;left:545px;top:53px;width:38px;height:38px;border-radius:50%;background:#E6E6E6;border:3px solid #D2D2D2}
h1{font-weight:600;font-size:28.5px;line-height:31px}
h2{font-weight:600;line-height:29px}
.accent{color:var(--orange)}
.form-box{position:absolute;left:96px;top:197px;width:442px;height:217px;background:var(--tint);border-radius:8px;overflow:hidden}
.field{position:absolute;height:23px;background:var(--white);border-bottom:1.5px solid var(--blue);font-size:9px;color:#555;padding:6px 6px;display:flex;justify-content:space-between;align-items:center}
.chev{width:6px;height:6px;border-right:1.5px solid var(--blue);border-bottom:1.5px solid var(--blue);transform:rotate(45deg);margin-top:-4px;margin-right:6px}
.photo{position:absolute;background:linear-gradient(160deg,#E8B660,#C98A2E 60%,#F2C230)}
.step{position:absolute;top:592px;width:125px;height:128px;background:var(--tint);border-radius:6px;text-align:center}
.step-num{width:20px;height:20px;border-radius:50%;background:var(--blue);color:var(--white);font-size:10px;margin:12px auto 0;display:flex;align-items:center;justify-content:center}
.step h3{font-weight:400;font-size:12px;line-height:17px;color:#333;margin-top:8px}
.step p{font-size:7.3px;line-height:12.5px;color:var(--muted);font-weight:300;margin-top:3px;padding:0 8px}
.feature{position:absolute;border-radius:6px;padding:14px 10px}
.feature.blue{background:var(--blue);color:var(--white)}
.feature.light{background:var(--tint);color:var(--ink)}
.star{width:17px;height:17px;border-radius:50%;display:flex;align-items:center;justify-content:center}
.feature.blue .star{background:var(--white);color:var(--blue)}
.feature.light .star{background:var(--ink);color:var(--white)}
.feature h4{font-weight:500;margin-top:8px}
.feature p{font-weight:300;margin-top:5px}
.mock{position:absolute;background:#F7FAFF;border:1px solid #DCE6F5;border-radius:6px;overflow:hidden;box-shadow:0 2px 8px rgba(20,99,243,.12)}
.mock .mt{font-size:4px;color:#333}
.mock-side{position:absolute;background:var(--white);border-radius:3px;box-shadow:0 1px 3px rgba(0,0,0,.08)}
.carrier{position:absolute;background:var(--white);border-radius:3px;border:1px solid #E5ECF7}
.bar{position:absolute;height:1px;background:linear-gradient(90deg,var(--green) 0 40%,#B8C6DA 40% 60%,var(--red) 60%)}
.mark{position:absolute;width:9px;height:9px;border-radius:2px;background:#D8E3F4}
.compare{position:absolute;left:72px;top:425px;width:332px;height:174px;background:var(--tint);border-radius:6px}
.col-rr{position:absolute;left:180px;top:15px;width:55px;height:142px;background:var(--orange)}
.trow{position:absolute;left:34px;width:270px;height:17.7px;border-bottom:1px solid var(--line);font-size:5.8px;color:#555;display:flex;align-items:center;padding-left:4px}
.trow .m{position:absolute;font-size:8px;width:55px;text-align:center}
.faq{position:absolute;left:72px;top:665px;width:332px;height:190px;background:var(--tint)}
.q{position:absolute;left:0;width:332px;height:17.6px;border-bottom:1px solid var(--blue);font-size:6.8px;color:#333;display:flex;align-items:center;justify-content:center}
.answer{position:absolute;left:67px;top:22px;font-size:5.6px;line-height:8.3px;color:#444;width:210px}
.answer ul{list-style:none}
.answer li::before{content:"• ";}
.answer li{padding-left:8px}
.cta{position:absolute;left:72px;top:886px;width:332px;height:91px;background:var(--blue);border-radius:6px;color:var(--white)}
.footer{position:absolute;left:38px;top:1008px;width:400px;height:128px;background:var(--tint)}
.fcol{position:absolute;top:12px;font-size:5.2px;line-height:9.3px;color:#555}
.fcol h5{font-size:7px;font-weight:500;color:#222;margin-bottom:3px}
</style>
</head>
<body>
<div class="canvas">
  <svg class="backdrop" width="1200" height="1200" viewBox="0 0 1200 1200" aria-hidden="true">
    <rect width="1200" height="1200" fill="#FFB54D"/>
    <polygon points="0,108 40,140 680,140 690,320 1160,150 1200,140 1200,1200 0,1200" fill="#1463F3"/>
  </svg>

  <section class="page page-left">
    <header class="nav">
      <div class="brand"><span class="brand-dot"></span>Quote Marlin</div>
      <span class="nav-link" style="left:210px">Car Insurance</span>
      <span class="nav-link" style="left:287px">Life Insurance</span>
      <span class="nav-link" style="left:363px">Resources</span>
      <span class="nav-link" style="left:423px">Company</span>
      <div class="btn nav-btn">Compare Now</div>
    </header>
    <div class="badge" role="img" aria-label="Award badge"></div>

    <div class="abs c" style="left:0;top:82px;width:634px">
      <h1>Compare Insurance Rates<br>Car, Home, Car <span class="accent">+</span> Home</h1>
      <p style="font-size:10.5px;line-height:14px;color:#333;margin-top:10px">See what you should pay at top insurance<br>companies near you</p>
    </div>

    <div class="form-box">
      <div class="field" style="left:45px;top:23px;width:161px">Zip Code</div>
      <div class="field" style="left:235px;top:23px;width:161px">Address</div>
      <div class="field" style="left:45px;top:58px;width:161px">Age</div>
      <div class="field" style="left:235px;top:58px;width:161px">Do you own a home?<span class="chev"></span></div>
      <div class="field" style="left:45px;top:93px;width:161px">Current Insurance Provider?<span class="chev"></span></div>
      <div class="field" style="left:235px;top:93px;width:161px">Credit Score?<span class="chev"></span></div>
      <div class="field" style="left:45px;top:128px;width:242px">Type of Insurance to Compare?<span class="chev"></span></div>
      <div class="btn" style="position:absolute;left:45px;top:170px;width:242px;height:23px;font-size:9px">See Your Results</div>
      <div class="abs" style="left:310px;top:161px;width:132px;height:56px;background:var(--blue);border-radius:6px 0 0 0"></div>
      <div class="photo" role="img" aria-label="Photo of a golden retriever wearing a yellow bandana" style="left:350px;top:121px;width:92px;height:96px;border-radius:40px 40px 0 0"></div>
    </div>

    <div class="abs c" style="left:0;top:456px;width:634px">
      <h2 style="font-size:23.6px">Insurance shopping can be pleasant<br>– like a relaxing scroll through the<br><span class="accent">best rates</span></h2>
      <p style="font-size:10.5px;margin-top:6px">Start saving in 3 simple steps</p>
    </div>
    <svg class="abs" style="left:154px;top:570px" width="322" height="8" aria-hidden="true">
      <circle cx="4" cy="4" r="3" fill="#111"/><circle cx="318" cy="4" r="3" fill="#111"/>
      <line x1="10" y1="4" x2="312" y2="4" stroke="#111" stroke-width="1" stroke-dasharray="6 5"/>
    </svg>

    <div class="step" style="left:96px"><div class="step-num">1</div><h3>Quick Start</h3><p>Answer 5 questions.<br>No phone number or<br>email required.</p></div>
    <div class="step" style="left:254px"><div class="step-num">2</div><h3>Retrieve Your<br>Rates</h3><p>We estimate how much<br>you'll pay at each top<br>provider in your state.</p></div>
    <div class="step" style="left:412px"><div class="step-num">3</div><h3>Compare and<br>Save</h3><p>Compare apples to<br>apples pricing to find<br>your next provider.</p></div>

    <div class="btn" style="position:absolute;left:196px;top:741px;width:242px;height:23px;font-size:9px">Get Started - Compare Now</div>

    <h2 class="abs c" style="left:0;top:805px;width:634px;font-size:24px">Everything you need to make the<br><span class="accent">right</span> decisions</h2>

    <div class="feature blue" style="left:96px;top:883px;width:259px;height:119px">
      <div class="star">★</div>
      <h4 style="font-size:9px;line-height:13px">No bait and switch – accurate rate estimates using better data</h4>
      <p style="font-size:6.8px;line-height:11.8px">No low-ball quotes. We use the rating plans submitted by each insurance carrier to the state department of insurance plus any applicable discounts to more accurately calculate what you can expect to pay.</p>
    </div>
    <div class="feature light" style="left:96px;top:1023px;width:259px;height:119px">
      <div class="star">★</div>
      <h4 style="font-size:9px;line-height:13px">No bait and switch – accurate rate estimates using better data</h4>
      <p style="font-size:6.8px;line-height:11.8px">No low-ball quotes. We use the rating plans submitted by each insurance carrier to the state department of insurance plus any applicable discounts to more accurately calculate what you can expect to pay.</p>
    </div>

    <div class="mock" style="left:376px;top:883px;width:190px;height:270px">
      <div class="abs mt" style="left:10px;top:6px;color:var(--blue);font-weight:600">Quote Marlin</div>
      <div class="abs mt" style="left:170px;top:6px">Menu</div>
      <div class="mock-side" style="left:10px;top:18px;width:45px;height:56px">
        <div class="abs mt" style="left:4px;top:4px">Go Back</div>
        <div class="abs" style="left:4px;top:44px;width:37px;height:5px;background:var(--blue);border-radius:2px"></div>
      </div>
      <div class="abs mt c" style="left:60px;top:20px;width:125px;font-size:4.5px">Range of Annual Rates</div>
      <div class="abs" style="left:64px;top:36px;width:116px;height:1px;background:var(--blue)"></div>
      <div class="abs mt" style="left:62px;top:52px;font-size:4.2px;font-weight:600">Your Results</div>
      <div class="carrier" style="left:60px;top:64px;width:125px;height:38px"><div class="abs mt" style="left:18px;top:3px">Harbor Lane Mutual</div><div class="bar" style="left:18px;top:20px;width:100px"></div></div>
      <div class="mark" style="left:60px;top:76px"></div>
      <div class="carrier" style="left:60px;top:107px;width:125px;height:38px"><div class="abs mt" style="left:18px;top:3px">Corvid Auto</div><div class="bar" style="left:18px;top:20px;width:100px"></div></div>
      <div class="mark" style="left:60px;top:119px;background:#1F57C8"></div>
      <div class="carrier" style="left:60px;top:150px;width:125px;height:38px"><div class="abs mt" style="left:18px;top:3px">Brindlecove</div><div class="bar" style="left:18px;top:20px;width:100px"></div></div>
      <div class="carrier" style="left:60px;top:193px;width:125px;height:38px"><div class="abs mt" style="left:18px;top:3px">Fieldstead</div><div class="bar" style="left:18px;top:20px;width:100px"></div></div>
      <div class="mark" style="left:60px;top:205px;background:#E04848"></div>
      <div class="carrier" style="left:60px;top:236px;width:125px;height:38px"><div class="abs mt" style="left:18px;top:3px">Tallowick</div><div class="bar" style="left:18px;top:20px;width:100px"></div></div>
    </div>
  </section>

  <section class="page page-right">
    <div class="feature blue" style="left:72px;top:22px;width:194px;height:89px;padding:8px 7px">
      <div class="star" style="width:13px;height:13px;font-size:8px">★</div>
      <h4 style="font-size:6.6px;line-height:10px;margin-top:5px">No bait and switch – accurate rate estimates using better data</h4>
      <p style="font-size:4.7px;line-height:8.8px;margin-top:3px">No low-ball quotes. We use the rating plans submitted by each insurance carrier to the state department of insurance plus any applicable discounts to more accurately calculate what you can expect to pay.</p>
    </div>
    <div class="feature light" style="left:72px;top:127px;width:194px;height:89px;padding:8px 7px">
      <div class="star" style="width:13px;height:13px;font-size:8px">★</div>
      <h4 style="font-size:6.6px;line-height:10px;margin-top:5px">No bait and switch – accurate rate estimates using better data</h4>
      <p style="font-size:4.7px;line-height:8.8px;margin-top:3px">No low-ball quotes. We use the rating plans submitted by each insurance carrier to the state department of insurance plus any applicable discounts to more accurately calculate what you can expect to pay.</p>
    </div>
    <div class="mock" style="left:282px;top:22px;width:142px;height:194px">
      <div class="abs mt" style="left:8px;top:4px;color:var(--blue);font-weight:600;font-size:3px">Quote Marlin</div>
      <div class="mock-side" style="left:8px;top:12px;width:34px;height:42px"><div class="abs" style="left:3px;top:32px;width:28px;height:4px;background:var(--blue)"></div></div>
      <div class="abs mt c" style="left:45px;top:14px;width:95px;font-size:3.2px">Range of Annual Rates</div>
      <div class="abs" style="left:48px;top:26px;width:88px;height:1px;background:var(--blue)"></div>
      <div class="carrier" style="left:45px;top:48px;width:94px;height:28px"><div class="bar" style="left:14px;top:14px;width:76px"></div></div>
      <div class="carrier" style="left:45px;top:80px;width:94px;height:28px"><div class="bar" style="left:14px;top:14px;width:76px"></div></div>
      <div class="mark" style="left:42px;top:88px;width:8px;height:8px;background:#1F57C8"></div>
      <div class="carrier" style="left:45px;top:112px;width:94px;height:28px"><div class="bar" style="left:14px;top:14px;width:76px"></div></div>
      <div class="carrier" style="left:45px;top:144px;width:94px;height:28px"><div class="bar" style="left:14px;top:14px;width:76px"></div></div>
      <div class="carrier" style="left:45px;top:176px;width:94px;height:28px"><div class="bar" style="left:14px;top:14px;width:76px"></div></div>
    </div>
    <div class="feature blue" style="left:72px;top:232px;width:352px;height:61px;padding:8px 7px">
      <div class="star" style="width:13px;height:13px;font-size:8px">★</div>
      <h4 style="font-size:6.6px;line-height:10px;margin-top:5px">No bait and switch – accurate rate estimates using better data</h4>
      <p style="font-size:4.7px;line-height:8.8px;margin-top:2px">No low-ball quotes. We use the rating plans submitted by each insurance carrier to the state department of insurance plus any applicable discounts to more accurately calculate what you can expect to pay.</p>
    </div>

    <div class="abs c" style="left:0;top:323px;width:476px">
      <h2 style="font-size:18.5px;line-height:22px">Your <span class="accent">free</span> and impartial insurance<br>research tool</h2>
      <p style="font-size:6.8px;line-height:10px;color:var(--muted);margin-top:5px">We're passionate about giving you open access to the data you need<br>to make smart insurance decisions. We don't sell insurance policies<br>directly – our tool allows you independently research your options<br>and seamlessly connect with the provider that works for you.</p>
    </div>

    <div class="compare">
      <div class="col-rr"></div>
      <div class="abs c" style="left:180px;top:19px;width:55px;font-size:6.5px;color:var(--white)">Quote Marlin</div>
      <div class="abs c" style="left:235px;top:19px;width:70px;font-size:6.5px">Other Companies</div>
      <div class="trow" style="top:33px">Connects you with the provider you choose<span class="m" style="left:146px;color:#fff">✓</span><span class="m" style="left:208px">✓</span></div>
      <div class="trow" style="top:51px">Connects you with the provider you choose<span class="m" style="left:146px;color:#fff">✓</span><span class="m" style="left:208px">✕</span></div>
      <div class="trow" style="top:68px">Connects you with the provider you choose<span class="m" style="left:146px;color:#fff">✓</span><span class="m" style="left:208px">✕</span></div>
      <div class="trow" style="top:86px">Connects you with the provider you choose<span class="m" style="left:146px;color:#fff">✓</span><span class="m" style="left:208px">✕</span></div>
      <div class="trow" style="top:104px">Connects you with the provider you choose<span class="m" style="left:146px;color:#fff">✓</span><span class="m" style="left:208px">✕</span></div>
      <div class="trow" style="top:122px">Connects you with the provider you choose<span class="m" style="left:146px;color:#fff">✓</span><span class="m" style="left:208px">✕</span></div>
      <div class="trow" style="top:139px;border-bottom:none">Connects you with the provider you choose<span class="m" style="left:146px;color:#fff">✕</span><span class="m" style="left:208px">✓</span></div>
    </div>

    <h2 class="abs c" style="left:0;top:628px;width:476px;font-size:18.5px">Frequently Asked Questions</h2>

    <div class="faq">
      <div class="q" style="top:0">How does the insurance company determine my rate?</div>
      <div class="answer">Car insurance companies determine how much they charge you based on your driver profile.<br>Factors that can impact your rates include:
        <ul>
          <li>Demographics – your age, home ownership, credit score, and more</li>
          <li>Your driving history – how long you've been driving, traffic violations, and more</li>
          <li>Your car – make, model, and year</li>
          <li>Where you live – state and zip code</li>
          <li>How much coverage you want</li>
        </ul>
      </div>
      <div class="abs" style="left:0;top:98px;width:332px;height:1px;background:var(--blue)"></div>
      <div class="q" style="top:101px">How does the insurance company determine my rate?</div>
      <div class="q" style="top:119px">How does the insurance company determine my rate?</div>
      <div class="q" style="top:137px">How does the insurance company determine my rate?</div>
      <div class="q" style="top:155px">How does the insurance company determine my rate?</div>
      <div class="q" style="top:172px">How does the insurance company determine my rate?</div>
    </div>

    <div class="cta">
      <div class="abs" style="left:15px;top:8px;font-size:19px;font-weight:600">Ready, set, retrieve</div>
      <div class="abs" style="left:15px;top:35px;font-size:7.8px;line-height:12px">Ready to get started? Dig up the best insurance<br>providers in seconds</div>
      <div class="abs" style="left:15px;top:63px;width:81px;height:17px;background:var(--white);color:#888;font-size:6.5px;padding:4px 5px">Zip Code</div>
      <div class="abs" style="left:96px;top:63px;width:73px;height:17px;background:var(--orange);font-size:6.5px;font-weight:500;display:flex;align-items:center;justify-content:center">See Your Results</div>
    </div>
    <div class="photo" role="img" aria-label="Photo of a golden retriever wearing a yellow bandana" style="left:286px;top:867px;width:93px;height:110px;border-radius:45px 45px 0 0"></div>

    <footer class="footer">
      <div class="fcol" style="left:34px;width:115px"><h5>About Quote Marlin</h5>Quote Marlin is your insurance companion – connecting you with top auto insurance providers without collecting your contact information.</div>
      <div class="fcol" style="left:169px"><h5>Resources</h5>FAQ<br>Insurance by state<br>Insurance by age<br>See all</div>
      <div class="fcol" style="left:236px"><h5>Support</h5>Contact Us<br>How we make money<br>Spam-free promise<br>Partner with Us</div>
      <div class="fcol" style="left:304px"><h5>Company</h5>Editorial policy<br>Accessibility statement<br>Cookie Policy<br>California residents:<br>Do not sell my info</div>
      <div class="fcol" style="left:169px;top:80px;width:220px"><h5>Find coverage in your state</h5>AL AK AZ AR CO CA CT DC DE FL GA HI ID IL IN IA KS KY LA ME MD MA MI MN MS MO MT NE NV NH NJ NM NY NC ND OH OK OR PA RI SC SD TN TX UT VT VA WA WV WI WY</div>
    </footer>
  </section>
</div>
</body>
</html>
```